Business Card Design Project

We need a business card design for an existing company in Dallas/Fort Worth that is expanding services and re-branding. We are changing the name from Brightmoor Commercial Cleaning to Keystride Facility Services. We are expanding from only commercial cleaning to include complete commercial landscape and facility maintenance services, too.

As stated, we offer a package of services that includes landscape, janitorial and facility services, which is largely unique in the industry.

We would like a design that communicates trust/partnership with a professional, corporate image, but not necessarily using the standard white business card. We would like a design that perhaps uses darker blues or perhaps a gray background, but we are open to other ideas. We might also be interested in a double-sided design - maybe with our logo on the back, printed on a gray background?

We will probably stick with the attached logo, but if you've got another inspired idea....

Target Market(s)

Property managers, commercial real estate professionals, corporate executives

Industry/Entity Type

Landscape

Requirements
Should not have
• Not interested in old style fonts.

```html
<!DOCTYPE html>
<html lang="en">
<head>
<meta charset="utf-8">
<title>Keystride Facility Services – Business Card</title>
<link href="https://fonts.googleapis.com/css2?family=Questrial&display=swap" rel="stylesheet">
<style>
  :root {
    --ink: #111111;
    --paper: #ffffff;
    --backdrop: #e9e6e1;
    --muted: #444444;
    --rule: #9a9a9a;
  }
  * { box-sizing: border-box; margin: 0; padding: 0; }
  html, body { width: 1200px; height: 900px; overflow: hidden; }
  body {
    background: var(--backdrop);
    font-family: "Questrial", "Century Gothic", sans-serif;
    color: var(--ink);
    position: relative;
  }
  .card {
    position: absolute;
    left: 260px;
    width: 680px;
    height: 389px;
    box-shadow: 0 8px 22px rgba(0,0,0,0.18);
    overflow: hidden;
  }
  .card--front { top: 45px; background: var(--paper); }
  .card--back { top: 466px; background: var(--ink); color: var(--paper); }

  .brand { position: absolute; }
  .brand__name { display: block; font-weight: 400; white-space: nowrap; }
  .brand__note { display: block; margin-top: 8px; white-space: nowrap; }

  .card--front .brand { left: 205px; top: 52px; }
  .card--front .brand__name { font-size: 30px; }
  .card--front .brand__note { font-size: 12px; color: var(--muted); }

  .holder { position: absolute; left: 40px; top: 162px; }
  .holder__marker {
    position: absolute; left: -40px; top: 6px;
    width: 0; height: 0;
    border-top: 11px solid transparent;
    border-bottom: 11px solid transparent;
    border-left: 16px solid var(--ink);
  }
  .holder__name { font-size: 28px; }
  .holder__title { font-size: 18px; color: var(--muted); margin-top: 2px; }

  .divider {
    position: absolute; left: 168px; top: 250px;
    width: 2px; height: 100px;
    background: linear-gradient(to bottom, transparent, var(--rule), transparent);
  }
  .contact { position: absolute; left: 190px; top: 240px; list-style: none; }
  .contact__item {
    display: flex; align-items: center; gap: 12px;
    font-size: 19px; height: 30px; white-space: nowrap;
  }
  .icon {
    width: 20px; height: 20px; border-radius: 5px;
    background: var(--ink); flex: none;
    display: inline-flex; align-items: center; justify-content: center;
  }
  .icon svg { width: 13px; height: 13px; }
  .contact__gap { margin-left: 18px; }

  .front-band {
    position: absolute; left: 0; bottom: 0;
    width: 100%; height: 12px; background: var(--ink);
  }

  .card--back .brand { left: 80px; top: 120px; }
  .card--back .brand__name { font-size: 40px; }
  .card--back .brand__note { font-size: 15px; color: #cfcfcf; }
  .back-web {
    position: absolute; left: 80px; top: 262px;
    font-size: 24px; letter-spacing: 0.5px;
  }
</style>
</head>
<body>

<section class="card card--front" aria-label="Business card front">
  <div class="brand">
    <span class="brand__name">Keystride Facility Services</span>
    <span class="brand__note">Grounds, cleaning and building care from a single partner</span>
  </div>

  <div class="holder">
    <span class="holder__marker"></span>
    <p class="holder__name">Martin Cole</p>
    <p class="holder__title">General Manager</p>
  </div>

  <span class="divider"></span>

  <ul class="contact">
    <li class="contact__item">
      <span class="icon"><svg viewBox="0 0 12 12"><path d="M6 1 1 5.5h1.6V11h2.6V8h1.6v3h2.6V5.5H11z" fill="#fff"/></svg></span>
      123 main st 000000 xxxxx 321 321
    </li>
    <li class="contact__item">
      <span class="icon"><svg viewBox="0 0 12 12"><path d="M3 1.2 4.8 3.6 3.8 4.8c.6 1.4 1.9 2.7 3.4 3.4l1.2-1 2.4 1.8-.9 1.8C5.6 10.6 1.4 6.4 1.2 2.1z" fill="#fff"/></svg></span>
      (000) 000-0000
      <span class="icon contact__gap"><svg viewBox="0 0 12 12"><rect x="3" y="1" width="6" height="3" fill="#fff"/><rect x="1" y="4.5" width="10" height="5" rx="1" fill="#fff"/><rect x="3" y="8" width="6" height="3" fill="#fff"/></svg></span>
      (000) 000-0000
    </li>
    <li class="contact__item">
      <span class="icon"><svg viewBox="0 0 12 12"><circle cx="6" cy="6" r="2" fill="none" stroke="#fff" stroke-width="1.3"/><path d="M8 4v2.8c0 1.2 2 1.2 2-.6A4 4 0 1 0 8.3 9.3" fill="none" stroke="#fff" stroke-width="1.3"/></svg></span>
      info@keystridefacilityservices.com.
    </li>
    <li class="contact__item">
      <span class="icon"><svg viewBox="0 0 12 12" fill="none" stroke="#fff" stroke-width="1.1"><circle cx="6" cy="6" r="4.8"/><ellipse cx="6" cy="6" rx="2" ry="4.8"/><path d="M1.2 6h9.6M2 3.5h8M2 8.5h8"/></svg></span>
      www.keystridefacilityservices.com.
    </li>
  </ul>

  <span class="front-band"></span>
</section>

<section class="card card--back" aria-label="Business card back">
  <div class="brand">
    <span class="brand__name">Keystride Facility Services</span>
    <span class="brand__note">Grounds, cleaning and building care from a single partner</span>
  </div>
  <p class="back-web">www.keystridefacilityservices.com.</p>
</section>

</body>
</html>
```